Fitness Training academy needs a business card design

We need a business card design for a NEW business that teaches/trains people how to become personal trainers. We would like to see designs both with and without our QR code. We would like our designs double sided.

See the following attachments
Design Brief
Logos (both black background, white background in all formats)
QR Code

Industry/Entity Type

Business

```html
<!DOCTYPE html>
<html lang="en">
<head>
<meta charset="utf-8">
<title>Ascend Trainer Institute – Business Card</title>
<link href="https://fonts.googleapis.com/css2?family=Michroma&family=Open+Sans:wght@400;600&display=swap" rel="stylesheet">
<style>
  :root {
    --backdrop: #2b2c2e;
    --card: #ffffff;
    --ink: #1e1e1e;
    --grey: #8a8a8a;
    --tab-grey: #8f8f8f;
    --accent-red: #e8262a;
    --accent-orange: #f57c1f;
    --icon: #ffffff;
  }
  * { box-sizing: border-box; margin: 0; padding: 0; }
  html, body {
    width: 1200px; height: 816px; overflow: hidden;
    background: var(--backdrop);
  }
  .canvas {
    width: 1200px; height: 816px;
    display: flex; align-items: center; justify-content: center;
  }
  .card {
    position: relative;
    width: 1050px; height: 600px;
    background: var(--card);
    border-radius: 34px;
    overflow: hidden;
  }
  .side-bar {
    position: absolute; left: 70px; top: 0;
    width: 58px; height: 540px;
    background: linear-gradient(180deg, var(--accent-red) 0%, var(--accent-orange) 55%, var(--accent-red) 100%);
    border-radius: 0 0 29px 29px;
  }
  .side-bar .icon {
    position: absolute; left: 15px; width: 28px; height: 28px;
  }
  .person-block {
    position: absolute; left: 158px; top: 58px;
    font-family: "Michroma", sans-serif; color: var(--ink);
  }
  .person-name { font-size: 27px; letter-spacing: 1px; line-height: 1.3; }
  .person-title { font-size: 25px; letter-spacing: 1px; line-height: 1.3; }
  .contact {
    position: absolute; left: 158px;
    font-family: "Open Sans", sans-serif; color: var(--ink);
    font-size: 24px; line-height: 1.35;
  }
  .contact-phone { top: 232px; }
  .contact-web { top: 330px; }
  .contact-address { top: 440px; }
  .brand {
    position: absolute; left: 590px; top: 150px;
    display: flex; flex-direction: column; align-items: flex-start;
  }
  .brand-row { display: flex; align-items: center; gap: 18px; }
  .brand-dot {
    width: 60px; height: 60px; border-radius: 50%;
    background: var(--accent-red);
  }
  .brand-name {
    font-family: "Michroma", sans-serif; font-size: 30px;
    color: var(--grey); letter-spacing: 1px; line-height: 1.25;
  }
  .brand-tagline {
    margin-top: 12px; margin-left: 78px;
    font-family: "Open Sans", sans-serif; font-size: 15px; font-weight: 600;
    letter-spacing: 5px; color: var(--grey);
  }
  .edge-tab {
    position: absolute; right: 0; top: 210px;
    width: 54px; height: 26px; background: var(--tab-grey);
  }
</style>
</head>
<body>
<main class="canvas">
  <article class="card">
    <div class="side-bar">
      <svg class="icon" style="top:60px" viewBox="0 0 24 24" aria-hidden="true"><circle cx="12" cy="8" r="4.5" fill="var(--icon)"/><path d="M3 22c0-5 4-8 9-8s9 3 9 8z" fill="var(--icon)"/></svg>
      <svg class="icon" style="top:275px" viewBox="0 0 24 24" aria-hidden="true"><path d="M6.6 3.5l3 3-1.8 2.4a13 13 0 0 0 7.3 7.3l2.4-1.8 3 3-2 2.6C11 19.5 4.5 13 3.5 5.5z" fill="var(--icon)"/></svg>
      <svg class="icon" style="top:335px" viewBox="0 0 24 24" aria-hidden="true"><rect x="2" y="5" width="20" height="14" rx="1" fill="var(--icon)"/><path d="M2.5 5.5 12 13l9.5-7.5" stroke="var(--accent-orange)" stroke-width="1.6" fill="none"/></svg>
      <svg class="icon" style="top:395px" viewBox="0 0 24 24" aria-hidden="true"><g fill="none" stroke="var(--icon)" stroke-width="1.8"><circle cx="12" cy="12" r="9.5"/><ellipse cx="12" cy="12" rx="4.2" ry="9.5"/><path d="M2.5 12h19M4 7h16M4 17h16"/></g></svg>
      <svg class="icon" style="top:460px" viewBox="0 0 24 24" aria-hidden="true"><path d="M12 3 2 12h3v9h5v-6h4v6h5v-9h3z" fill="var(--icon)"/></svg>
    </div>

    <div class="person-block">
      <p class="person-name">jordan reyes</p>
      <p class="person-title">GENERAL MANAGER</p>
    </div>
    <p class="contact contact-phone">+2 (0123) 45-678-90</p>
    <p class="contact contact-web">hello@ascendtrainer.example<br>www.ascendtrainer.example</p>
    <p class="contact contact-address">1450 Harbor Lane,<br>Eastfield, USA</p>

    <div class="brand">
      <div class="brand-row">
        <span class="brand-dot"></span>
        <p class="brand-name">ASCEND TRAINER<br>INSTITUTE</p>
      </div>
      <p class="brand-tagline">SHAPING FUTURE COACHES</p>
    </div>

    <span class="edge-tab"></span>
  </article>
</main>
</body>
</html>
```